FSA Expiring Soon 2023

Hi,
Looking to upgrade the design of current flyer to be used as an e-blast.
-8.5"x11"
-Under 5MB
-Several formats, PDF, .ai, jpeg, png

This flyer should be simple, yet eye catching. The goal is to remind patients that their Flexible Spending Account (FSA) will be expiring soon and that they can use their FSA or HSA to purchase most of our over the counter items, including inserts and shoes.

-must include: Some insurance plans require a letter of medical necessity
-must include: Each flexible spending account varies on their expiration date
- stock images must be free

I'll attach our logo and old flyer as well for reference.

Thank you,
Oscar

```html
<!DOCTYPE html>
<html lang="en">
<head>
<meta charset="utf-8">
<title>FSA Expires Soon – Stonebrook Foot &amp; Ankle</title>
<link rel="stylesheet" href="https://fonts.googleapis.com/css2?family=Lato:wght@400;700;900&family=Roboto:wght@500;700&display=swap">
<style>
  :root {
    --orange: #f47f45;
    --teal: #58c1a6;
    --ink: #1c1c1c;
    --white: #ffffff;
    --photo-skin: #e9d6c9;
    --photo-wood: #9a7656;
  }
  * { box-sizing: border-box; margin: 0; padding: 0; }
  html, body { width: 927px; height: 1200px; overflow: hidden; background: var(--white); }
  .flyer { position: relative; width: 927px; height: 1200px; font-family: "Lato", Arial, sans-serif; color: var(--ink); overflow: hidden; }

  .brand { position: absolute; left: 48px; top: 26px; display: flex; align-items: center; gap: 14px; }
  .brand-mark { width: 40px; height: 40px; background: var(--teal); }
  .brand-name { font-weight: 900; font-size: 30px; line-height: 1; color: var(--orange); }
  .brand-web { position: absolute; left: 102px; top: 70px; font-weight: 700; font-size: 12px; color: var(--orange); letter-spacing: .5px; }

  .call { position: absolute; left: 624px; top: 34px; display: flex; align-items: center; gap: 22px; }
  .call-icon { width: 50px; height: 50px; border-radius: 10px; background: var(--orange); display: flex; align-items: center; justify-content: center; }
  .call-label { font-size: 14px; font-weight: 700; color: var(--orange); }
  .call-number { font-size: 25px; font-weight: 700; color: var(--orange); margin-top: 4px; }

  .photo { position: absolute; box-shadow: 0 6px 14px rgba(0,0,0,.18); }
  .photo-exam { left: 45px; top: 129px; width: 250px; height: 220px; border: 3px solid var(--teal); background: linear-gradient(135deg, #f2f2f2, var(--photo-skin) 55%, #3a3a3a); clip-path: polygon(0 0, 100% 4%, 100% 96%, 0 100%); }
  .photo-blocks { left: 326px; top: 129px; width: 254px; height: 164px; border: 3px solid var(--orange); background: linear-gradient(180deg, #d9d5d0 0%, #cfc8c0 55%, var(--photo-wood) 75%, #6e5038 100%); }
  .photo-sole { left: 624px; top: 129px; width: 260px; height: 218px; border: 3px solid var(--teal); background: linear-gradient(160deg, #f3eee9, var(--photo-skin) 50%, #d7b6a3); clip-path: polygon(0 0, 100% 0, 100% 100%, 0 92%); }

  .lead { position: absolute; left: 0; top: 346px; width: 927px; text-align: center; font-size: 25px; font-weight: 700; line-height: 46px; color: var(--ink); }

  .banner { position: absolute; left: 0; top: 448px; width: 927px; height: 196px; }
  .banner-title { position: absolute; left: 0; top: 512px; width: 927px; text-align: center; font-weight: 700; font-size: 52px; color: var(--white); }

  .intro { position: absolute; left: 40px; top: 690px; font-size: 19.5px; color: var(--ink); }
  .points { position: absolute; left: 50px; top: 740px; list-style: none; }
  .points li { display: flex; align-items: center; gap: 18px; height: 51px; font-size: 20px; color: var(--orange); }

  .cta { position: absolute; left: 217px; top: 853px; width: 426px; height: 78px; border: 4px solid var(--orange); border-radius: 16px; background: var(--teal); color: var(--white); font-family: "Roboto", Arial, sans-serif; font-weight: 500; font-size: 27px; display: flex; align-items: center; justify-content: center; box-shadow: 0 4px 8px rgba(0,0,0,.15); }

  .offices { position: absolute; left: 0; top: 998px; width: 927px; height: 146px; background: var(--teal); display: flex; }
  .office { flex: 1; color: var(--white); padding-top: 26px; }
  .office + .office { border-left: 4px solid var(--white); }
  .office:nth-child(1) { padding-left: 46px; }
  .office:nth-child(2) { text-align: center; }
  .office:nth-child(3) { text-align: right; padding-right: 44px; }
  .office-name { font-weight: 700; font-size: 20px; margin-bottom: 10px; }
  .office-address { font-weight: 700; font-size: 15.5px; line-height: 27px; }

  .footer { position: absolute; left: 0; top: 1144px; width: 927px; height: 56px; background: var(--orange); color: var(--white); font-weight: 700; font-size: 22px; display: flex; align-items: center; justify-content: space-between; padding: 0 44px; }
</style>
</head>
<body>
<main class="flyer">
  <header>
    <div class="brand">
      <span class="brand-mark"></span>
      <span class="brand-name">STONEBROOK FOOT &amp; ANKLE</span>
    </div>
    <div class="brand-web">STRIDEWELLFEET.COM</div>
    <div class="call">
      <div class="call-icon">
        <svg width="28" height="28" viewBox="0 0 24 24" aria-hidden="true"><path fill="#fff" d="M6.6 10.8a15.1 15.1 0 0 0 6.6 6.6l2.2-2.2a1 1 0 0 1 1-.25 11.4 11.4 0 0 0 3.6.57 1 1 0 0 1 1 1V20a1 1 0 0 1-1 1A17 17 0 0 1 3 4a1 1 0 0 1 1-1h3.5a1 1 0 0 1 1 1c0 1.25.2 2.45.57 3.57a1 1 0 0 1-.25 1z"/></svg>
      </div>
      <div>
        <div class="call-label">CALL TODAY</div>
        <div class="call-number">(877)555-0142</div>
      </div>
    </div>
  </header>

  <div class="photo photo-exam" role="img" aria-label="Gloved podiatrist examining a patient's foot"></div>
  <div class="photo photo-blocks" role="img" aria-label="Wooden letter blocks spelling FSA and HSA on a table"></div>
  <div class="photo photo-sole" role="img" aria-label="Gloved hands applying a pad to the sole of a foot"></div>

  <p class="lead">Use your Flexible spending Account funds before<br>they expire at tee end of tee year!</p>

  <svg class="banner" viewBox="0 0 927 196" preserveAspectRatio="none" aria-hidden="true">
    <path fill="#f47f45" d="M0 48 L60 44 L140 50 L230 40 L300 30 L360 24 L420 14 L470 8 L520 4 L560 2 L600 0 L640 6 L690 10 L730 20 L770 26 L820 22 L870 30 L927 26 L927 150 L880 154 L840 150 L790 158 L740 156 L700 164 L650 160 L600 168 L560 176 L520 184 L480 194 L450 196 L420 188 L390 176 L350 166 L310 160 L270 164 L230 160 L190 156 L140 160 L100 156 L60 160 L0 158 Z"/>
  </svg>
  <h1 class="banner-title">Expires Soon!</h1>

  <p class="intro">Most of our over-the-counter products are FSA/HSA eligible, including orthotics and shoes.</p>
  <ul class="points">
    <li><svg width="16" height="14" viewBox="0 0 16 14" aria-hidden="true"><path d="M1.5 7.5 L6 12 L14.5 2" fill="none" stroke="#f47f45" stroke-width="3" stroke-linecap="round" stroke-linejoin="round"/></svg>Some insurance plans require a letter of medical necessity</li>
    <li><svg width="16" height="14" viewBox="0 0 16 14" aria-hidden="true"><path d="M1.5 7.5 L6 12 L14.5 2" fill="none" stroke="#f47f45" stroke-width="3" stroke-linecap="round" stroke-linejoin="round"/></svg>Each flexible spending account varies on their expiration date</li>
  </ul>

  <div class="cta">REQUEST AN APPOINTMENT</div>

  <section class="offices">
    <div class="office">
      <div class="office-name">Stonebrook Office</div>
      <div class="office-address">218 Harlow Mill Dr.<br>Ste. 140 Stonebrook, MD 21790</div>
    </div>
    <div class="office">
      <div class="office-name">Linden Office</div>
      <div class="office-address">5120 Ashcroft Blvd.<br>Ste. 305, Linden, MD 21795</div>
    </div>
    <div class="office">
      <div class="office-name">Cedar Ridge Office</div>
      <div class="office-address">476 Wellness Way<br>Cedar Ridge, WV 25490</div>
    </div>
  </section>

  <footer class="footer">
    <span>StrideWellFeet.com</span>
    <span>(877)555-0142</span>
  </footer>
</main>
</body>
</html>
```